Business Consulting Company needs a business card designed

We need a business card in Brisbane Australia for a company called " Brindlewood Consulting Group". I would like to see the designs either in purple or green color

```html
<!DOCTYPE html>
<html lang="en">
<head>
<meta charset="utf-8">
<title>Brindlewood Consulting Group – Business Card</title>
<link rel="stylesheet" href="https://fonts.googleapis.com/css2?family=Open+Sans:wght@300;400;600;700&display=swap">
<style>
  :root {
    --sage: #c3c985;
    --sage-deep: #b7bd76;
    --paper: #ffffff;
    --ink: #1f1f1f;
    --ink-soft: #4a4a4a;
    --backdrop: #e6e6e4;
  }
  * { box-sizing: border-box; margin: 0; padding: 0; }
  html, body {
    width: 1200px; height: 720px; overflow: hidden;
    background: var(--backdrop);
    font-family: "Open Sans", Arial, sans-serif;
  }
  .stage {
    width: 1200px; height: 720px;
    display: flex; align-items: center; justify-content: center; gap: 40px;
  }
  .card {
    width: 520px; height: 297px; position: relative; overflow: hidden;
    box-shadow: 0 6px 18px rgba(0,0,0,.18);
  }

  /* Front */
  .card--front { background: var(--sage); display: flex; align-items: center; justify-content: center; }
  .front-mark { display: flex; flex-direction: column; align-items: center; gap: 14px; }
  .front-mark__dot { width: 74px; height: 74px; border-radius: 50%; background: var(--paper); }
  .front-mark__name {
    color: var(--paper); font-weight: 400; font-size: 19px;
    letter-spacing: 3px; text-transform: uppercase;
  }

  /* Back */
  .card--back { background: var(--paper); }
  .back-disc {
    position: absolute; left: -70px; top: 62px;
    width: 250px; height: 250px; border-radius: 50%; background: var(--sage);
  }
  .holder { position: absolute; left: 28px; top: 20px; }
  .holder__name { font-size: 21px; color: var(--ink); font-weight: 300; letter-spacing: .2px; }
  .holder__name strong { font-weight: 700; font-style: italic; }
  .holder__role { font-size: 13px; color: var(--ink-soft); font-weight: 300; margin-top: -2px; }

  .details {
    position: absolute; right: 30px; bottom: 22px; text-align: right;
    color: var(--ink); font-size: 12.5px; line-height: 1.45;
  }
  .brand { display: flex; align-items: center; justify-content: flex-end; gap: 10px; margin-bottom: 12px; }
  .brand__dot { width: 30px; height: 30px; border-radius: 50%; background: var(--sage); }
  .brand__name { font-size: 11px; font-weight: 600; letter-spacing: 1.2px; text-transform: uppercase; color: var(--ink); }
  .address { margin-bottom: 10px; }
  .contact dt { display: inline; font-weight: 700; }
  .contact dd { display: inline; margin: 0; }
  .contact .web { font-weight: 700; }
</style>
</head>
<body>
<main class="stage">
  <section class="card card--front" aria-label="Card front">
    <div class="front-mark">
      <span class="front-mark__dot"></span>
      <span class="front-mark__name">Brindlewood Consulting Group</span>
    </div>
  </section>

  <section class="card card--back" aria-label="Card back">
    <span class="back-disc"></span>
    <div class="holder">
      <p class="holder__name"><strong>Mara</strong> Ellison</p>
      <p class="holder__role">CEO</p>
    </div>
    <div class="details">
      <div class="brand">
        <span class="brand__name">Brindlewood Consulting Group</span>
        <span class="brand__dot"></span>
      </div>
      <p class="address">58 Harbour Ln,<br>Tingalpa Queensland<br>4173 Australia</p>
      <dl class="contact">
        <div><dt>T :</dt> <dd>3041227815</dd></div>
        <div><dt>M :</dt> <dd>9062418307</dd></div>
        <div><dt>E :</dt> <dd>mara@brindlewoodconsulting.com</dd></div>
        <div class="web">www.brindlewoodconsulting.com</div>
      </dl>
    </div>
  </section>
</main>
</body>
</html>
```